School Learner profile graphic representation

I have a set of ideas around communicating our school 'learner profile'. These represent the attitudes, habits and dispositions we are trying to develop through our curriculum and wider enrichment programme. I want the links between the ideas and concepts to be represented in some form of an inforgraphic which can be published and displayed for the whole community to connect with. we run two schools and want the profile to represent for both.

Target Market(s)

Students, Parents, Teachers, Wider community in education

Industry/Entity Type

Education

Font styles to use
Other font styles liked:
• Johnson p22

Colors

Designer to choose colors to be used in the design.

Requirements
Must have
• See my diagram in the ppt.
• The statements Aspiration, Agency, Agility, Altitude with the supporting descriptions. Ideally the values in the center is also represented. The two school logos should also be present somehow (both emblems at least). Let me know if the full logo files are required
Nice to have
• the numbering shown in my diagram is not absolutely necessary is it is not necessarily a linear process and rather cyclical and cross reinforcing

```html
<!DOCTYPE html>
<html lang="en">
<head>
<meta charset="utf-8">
<title>Envisioning Our Learners</title>
<link rel="stylesheet" href="https://fonts.googleapis.com/css2?family=Montserrat:wght@500;600;700;800&display=swap">
<style>
  :root {
    --brand-red: #e3262d;
    --label-red: #de3a1c;
    --teal: #3aa8b8;
    --green: #22b35e;
    --yellow: #e5cc00;
    --blue: #1a78c2;
    --ink: #2b2b2b;
    --muted: #5a5a5a;
    --rule: #a9a9a9;
    --paper: #ffffff;
  }
  html, body { margin: 0; padding: 0; overflow: hidden; background: var(--paper); }
  .canvas {
    position: relative; width: 1200px; height: 817px; overflow: hidden;
    background: var(--paper); font-family: "Montserrat", sans-serif;
  }
  .schools { position: absolute; left: 56px; top: 72px; }
  .school {
    display: flex; align-items: center; gap: 10px;
    color: var(--brand-red); font-weight: 700; font-size: 18px; line-height: 1;
    margin-bottom: 22px; white-space: nowrap;
  }
  .school-dot { width: 20px; height: 20px; border-radius: 50%; background: var(--brand-red); }
  .divider { position: absolute; left: 314px; top: 58px; width: 2px; height: 108px; background: #c8c8c8; }
  .headline {
    position: absolute; left: 342px; top: 84px; margin: 0;
    color: var(--brand-red); font-weight: 600; font-size: 45px; letter-spacing: 1.5px; line-height: 1;
  }
  .cycle { position: absolute; left: 0; top: 0; }
  .ring-label { fill: var(--paper); font-weight: 800; letter-spacing: 3px; }
  .core-word { fill: var(--blue); font-weight: 700; font-size: 28px; }
  .traits { position: absolute; left: 678px; top: 160px; width: 450px; }
  .trait { position: relative; height: 158px; border-bottom: 1px solid var(--rule); }
  .trait:last-child { border-bottom: none; }
  .trait-text { position: absolute; left: 121px; top: 22px; }
  .trait-lead { color: var(--muted); font-size: 19px; font-weight: 500; line-height: 1; }
  .trait-name { color: var(--label-red); font-size: 27px; font-weight: 700; letter-spacing: 1.5px; line-height: 1; margin-top: 7px; }
  .trait-desc { color: var(--ink); font-size: 17px; font-weight: 500; line-height: 24px; margin-top: 7px; }
  .trait-icon { position: absolute; left: 8px; top: 22px; width: 90px; height: 118px; border-radius: 12px; }
  .icon-agency { background: linear-gradient(160deg, #4bb3c2, var(--teal)); }
  .icon-aspiration { background: linear-gradient(180deg, #9fd3db, #7fcf9c); }
  .icon-agility { background: linear-gradient(160deg, #5cc585, #c9d85a); }
  .icon-altitude { background: linear-gradient(180deg, #f3b1b3, #ecd866); }
</style>
</head>
<body>
<div class="canvas">
  <div class="schools">
    <div class="school"><span class="school-dot"></span>Cedar Grove Academy</div>
    <div class="school"><span class="school-dot"></span>Hillview School</div>
  </div>
  <div class="divider"></div>
  <h1 class="headline">ENVISIONING OUR LEARNERS</h1>

  <svg class="cycle" width="680" height="817" viewBox="0 0 680 817">
    <defs>
      <path id="arc-mind" d="M 168 485 A 172 172 0 0 1 265 330"/>
      <path id="arc-heart" d="M 439 344 A 172 172 0 0 1 504 535"/>
      <path id="arc-attitude-outer" d="M 476 599 A 178 178 0 0 1 168 531"/>
      <path id="arc-attitude-inner" d="M 431 576 A 128 128 0 0 1 220 529"/>
    </defs>
    <g fill="none" stroke-width="150">
      <circle cx="340" cy="485" r="190" stroke="var(--teal)" stroke-dasharray="434.1 1193.8" transform="rotate(153 340 485)"/>
      <circle cx="340" cy="485" r="190" stroke="var(--green)" stroke-dasharray="444.1 1193.8" transform="rotate(272 340 485)"/>
      <circle cx="340" cy="485" r="190" stroke="var(--yellow)" stroke-dasharray="391 1193.8" transform="rotate(40 340 485)"/>
    </g>
    <circle cx="386" cy="301" r="75" fill="var(--teal)"/>
    <circle cx="472" cy="622" r="75" fill="var(--green)"/>
    <circle cx="164" cy="556" r="75" fill="var(--yellow)"/>
    <circle cx="338" cy="485" r="110" fill="var(--paper)"/>

    <text class="ring-label" font-size="56"><textPath href="#arc-mind" startOffset="50%" text-anchor="middle">MIND</textPath></text>
    <text class="ring-label" font-size="56"><textPath href="#arc-heart" startOffset="50%" text-anchor="middle">HEART</textPath></text>
    <text class="ring-label" font-size="48"><textPath href="#arc-attitude-outer" startOffset="50%" text-anchor="middle">ATTITUDE</textPath></text>
    <text class="ring-label" font-size="34"><textPath href="#arc-attitude-inner" startOffset="50%" text-anchor="middle">AND SPIRIT</textPath></text>

    <g text-anchor="middle">
      <text class="core-word" x="338" y="447">VALUES</text>
      <text class="core-word" x="338" y="481">MORALS</text>
      <text class="core-word" x="338" y="515">PRINCIPLES</text>
      <text class="core-word" x="338" y="548">ETHICS</text>
    </g>
  </svg>

  <div class="traits">
    <div class="trait">
      <div class="trait-icon icon-agency" role="img" aria-label="Illustration of a thinking head with a gear and stars"></div>
      <div class="trait-text">
        <div class="trait-lead">Learners with</div>
        <div class="trait-name">AGENCY</div>
        <div class="trait-desc">Believe in their capacity and<br>responsibility to do great things</div>
      </div>
    </div>
    <div class="trait">
      <div class="trait-icon icon-aspiration" role="img" aria-label="Illustration of a ladder reaching up to a cloud"></div>
      <div class="trait-text">
        <div class="trait-lead">Learners with</div>
        <div class="trait-name">ASPIRATION</div>
        <div class="trait-desc">Inspired and believe in<br>pursuing great things</div>
      </div>
    </div>
    <div class="trait">
      <div class="trait-icon icon-agility" role="img" aria-label="Illustration of an arrow striking a target"></div>
      <div class="trait-text">
        <div class="trait-lead">Learners with</div>
        <div class="trait-name">AGILITY</div>
        <div class="trait-desc">Are deterined, equipped and able<br>to accomplish great things</div>
      </div>
    </div>
    <div class="trait">
      <div class="trait-icon icon-altitude" role="img" aria-label="Illustration of mountain peaks with a flag at the summit"></div>
      <div class="trait-text">
        <div class="trait-lead">Learners with</div>
        <div class="trait-name">ALTITUDE</div>
        <div class="trait-desc">Achieve Great things and<br>work to elevate others</div>
      </div>
    </div>
  </div>
</div>
</body>
</html>
```